2 sided postcard for New Internet Customers

We would like a design for a two sided postcard (with room for mailing label), dimensions 9 1/4 by 6 1/4 to be sent via US Mail.

The postcard needs to include our logo (attached) and the text
Fiber Optic Internet
555-219-8063
http://www.brightwirenet.example
Speeds up to 1 Gig, with packages starting at $55

These will be sent to people who do not have our service.

Since this is going to be "junk mail" we probably only have 1 second or less to capture someone's attention to encourage them to read the entire postcard.

We are a "mom and pop" telecommunications company that provides internet, phone, and television services on the fiber optic network that we designed, built, and maintain.

We started as a dial up ISP in 1995, and have extraordinary technical support based in Freeport PA, our customers actually get the speeds they pay for, and our service is highly reliable.

We have a slogan (which you can choose to use or ignore) which is
"I Went Fast with Kornwell"

Existing customers can earn a $50 credit for every new customer they refer to us. Unlike most large cable and internet companies we have very happy customers... some who have stayed with us for decades.

I've attached our previous postcard, which I really dislike. It does have a blank spot for where the mailing label should go.

Target Market(s)

New Internet Customers in Western Pennsylvania

Industry/Entity Type

Internet

Font styles to use
Other font styles liked:
• Just match our logo.

Colors

Designer to choose colors to be used in the design.

Requirements
Must have
• The postcard needs to include our logo, and the text Fiber Optic Internet 555-219-8063 http://www.brightwirenet.example Speeds up to 1 Gig, with packages starting at $55
Nice to have
• The colors and fonts should look good with our logo.
Should not have
• Should not have small print or lots of text. Both sides need to capture attention.

```html
<!DOCTYPE html>
<html lang="en">
<head>
<meta charset="utf-8">
<title>Kornwell Fiber Optic Internet Postcard</title>
<link href="https://fonts.googleapis.com/css2?family=Montserrat:ital,wght@0,500;0,700;0,800;1,800;1,900&family=Roboto:wght@400;500;700&display=swap" rel="stylesheet">
<style>
  :root{
    --navy:#0a1a3a;
    --navy-deep:#050d22;
    --blue:#1f6fd6;
    --blue-bright:#2b8cff;
    --white:#ffffff;
    --ink:#1c2433;
    --grey:#6b7380;
    --line:#c9ced6;
    --stage:#eceef1;
  }
  *{box-sizing:border-box;margin:0;padding:0}
  html,body{width:675px;height:1200px;overflow:hidden}
  body{background:var(--stage);font-family:"Roboto",Arial,sans-serif;position:relative}
  .card{position:absolute;left:57px;width:560px;height:378px;overflow:hidden;box-shadow:0 4px 14px rgba(0,0,0,.18)}
  .card--front{top:202px;background:var(--navy-deep)}
  .card--back{top:620px;background:var(--white)}

  /* front */
  .front-photo{position:absolute;inset:0;background:
      radial-gradient(ellipse at 30% 70%,rgba(255,190,120,.55),transparent 35%),
      radial-gradient(ellipse at 65% 55%,rgba(80,150,255,.35),transparent 45%),
      linear-gradient(160deg,#0b1d44 0%,#06112b 55%,#0a1a3a 100%)}
  .brand{position:absolute;left:22px;top:20px;color:var(--white)}
  .brand__row{display:flex;align-items:center;gap:8px}
  .brand__dot{width:26px;height:26px;border-radius:50%;background:var(--blue-bright)}
  .brand__name{font-family:"Montserrat",sans-serif;font-weight:700;font-size:19px}
  .brand__url{font-size:9px;margin:2px 0 4px 34px;opacity:.85}
  .brand__tag{display:inline-block;background:var(--blue);font-family:"Montserrat",sans-serif;font-weight:700;font-size:13px;padding:3px 10px;margin-left:4px}
  .brand__phone{font-size:11px;font-weight:700;margin:4px 0 0 8px}
  .headline{position:absolute;right:26px;top:18px;text-align:right;font-family:"Montserrat",sans-serif;font-style:italic;font-weight:900;line-height:.95}
  .headline__top{color:var(--white);font-size:34px}
  .headline__bottom{color:var(--blue-bright);font-size:48px}
  .front-wave{position:absolute;left:0;bottom:0;width:560px;height:150px}
  .offer{position:absolute;right:26px;bottom:20px;text-align:right;color:var(--white)}
  .offer__badge{display:inline-block;background:var(--blue-bright);font-size:9px;font-weight:700;padding:2px 7px;border-radius:3px}
  .offer__sub{font-size:12px;font-weight:500;margin-top:3px}
  .offer__price{font-family:"Montserrat",sans-serif;font-weight:800;font-size:28px;line-height:1.05}

  /* back */
  .back-left{position:absolute;left:0;top:0;width:290px;height:378px}
  .back-photo{position:absolute;left:0;top:0;width:290px;height:120px;background:linear-gradient(135deg,#cfe0f7,#5a9ae8 55%,#2a63c0)}
  .back-photo-wave{position:absolute;left:0;top:80px;width:290px;height:50px}
  .services{position:absolute;left:18px;top:132px;width:256px}
  .services__title{font-family:"Montserrat",sans-serif;font-weight:800;font-size:13px;color:var(--navy)}
  .services__rule{width:34px;height:2px;background:var(--blue);margin:3px 0 6px}
  .services__text{font-size:7px;line-height:1.45;color:var(--grey)}
  .services__grid{display:flex;gap:6px;margin:10px 0}
  .service{flex:1;height:62px;background:var(--blue);color:var(--white);display:flex;flex-direction:column;align-items:center;justify-content:center;gap:5px;font-size:7px;font-weight:500;text-align:center}
  .service svg{width:20px;height:20px}
  .back-bar{position:absolute;left:0;bottom:0;width:290px;height:26px;background:var(--navy);color:var(--white);display:flex;align-items:center;justify-content:space-between;padding:0 14px;font-size:8.5px;font-weight:500}
  .back-bar span{display:flex;align-items:center;gap:4px}
  .divider{position:absolute;left:300px;top:24px;width:1px;height:330px;background:var(--line)}
  .back-brand{position:absolute;left:316px;top:24px;color:var(--navy)}
  .back-brand .brand__name{font-size:14px}
  .back-brand .brand__dot{width:20px;height:20px}
  .back-brand .brand__url{margin-left:28px;font-size:7px;color:var(--grey)}
  .back-brand .brand__tag{font-size:10px;color:var(--white)}
  .back-brand .brand__phone{font-size:9px;color:var(--ink)}
  .stamp{position:absolute;right:22px;top:24px;width:44px;height:50px;border:1px solid var(--line);background:#f4f5f7}
  .address-line{position:absolute;left:370px;width:160px;height:1px;background:var(--line)}
</style>
</head>
<body>

<section class="card card--front" aria-label="Postcard front">
  <div class="front-photo" role="img" aria-label="Photo of a hand touching a glowing network of connected nodes over a city at night"></div>

  <div class="brand">
    <div class="brand__row"><span class="brand__dot"></span><span class="brand__name">Kornwell, Inc.</span></div>
    <div class="brand__url">www.kornwell.example</div>
    <div class="brand__tag">Internet Services</div>
    <div class="brand__phone">(555) 304-7712</div>
  </div>

  <h1 class="headline">
    <div class="headline__top">FIBER OPTIC</div>
    <div class="headline__bottom">INTERNET</div>
  </h1>

  <svg class="front-wave" viewBox="0 0 560 150" preserveAspectRatio="none" aria-hidden="true">
    <path d="M0 104 C180 76 330 26 560 6 L560 150 L0 150Z" fill="#2b8cff" opacity=".45"/>
    <path d="M0 124 C180 94 330 44 560 24 L560 150 L0 150Z" fill="#1f6fd6"/>
    <path d="M0 120 C180 90 330 40 560 20" fill="none" stroke="#ffffff" stroke-width="2"/>
  </svg>

  <div class="offer">
    <div class="offer__badge">Speeds up to</div>
    <div class="offer__sub">1 Gig, with packages</div>
    <div class="offer__price">Starting at $55</div>
  </div>
</section>

<section class="card card--back" aria-label="Postcard back">
  <div class="back-left">
    <div class="back-photo" role="img" aria-label="Photo of blue fiber optic network cables plugged into a switch"></div>
    <svg class="back-photo-wave" viewBox="0 0 290 50" preserveAspectRatio="none" aria-hidden="true">
      <path d="M0 30 C90 0 180 50 290 14 L290 50 L0 50Z" fill="#1f6fd6"/>
      <path d="M0 38 C90 10 180 56 290 24 L290 50 L0 50Z" fill="#ffffff"/>
    </svg>

    <div class="services">
      <h2 class="services__title">OUR SERVICES</h2>
      <div class="services__rule"></div>
      <p class="services__text">We are a local fiber provider that designed, built and maintains its own network, with friendly support right here at home.</p>
      <div class="services__grid">
        <div class="service">
          <svg viewBox="0 0 24 24" fill="none" stroke="#fff" stroke-width="1.6"><circle cx="12" cy="12" r="9"/><path d="M3 12h18M12 3c3 3 3 15 0 18M12 3c-3 3-3 15 0 18"/></svg>
          Fiber Internet
        </div>
        <div class="service">
          <svg viewBox="0 0 24 24" fill="none" stroke="#fff" stroke-width="1.6"><rect x="4" y="4" width="16" height="6" rx="1"/><rect x="4" y="14" width="16" height="6" rx="1"/><circle cx="8" cy="7" r=".8" fill="#fff"/><circle cx="8" cy="17" r=".8" fill="#fff"/></svg>
          Managed Hosting
        </div>
        <div class="service">
          <svg viewBox="0 0 24 24" fill="none" stroke="#fff" stroke-width="1.6"><path d="M6 3h4l2 5-3 2a11 11 0 0 0 5 5l2-3 5 2v4a2 2 0 0 1-2 2A17 17 0 0 1 4 5a2 2 0 0 1 2-2z"/></svg>
          Phone Service
        </div>
        <div class="service">
          <svg viewBox="0 0 24 24" fill="none" stroke="#fff" stroke-width="1.6"><rect x="3" y="5" width="18" height="12" rx="1"/><path d="M8 21h8M12 17v4"/></svg>
          Cable Television
        </div>
      </div>
      <p class="services__text">Refer a friend and earn a $50 credit for every new customer who joins. Call today to check service at your address.</p>
    </div>

    <div class="back-bar">
      <span><svg width="9" height="9" viewBox="0 0 24 24" fill="#fff"><path d="M6 2h4l2 6-3 2a12 12 0 0 0 5 5l2-3 6 2v4a2 2 0 0 1-2 2A18 18 0 0 1 4 4a2 2 0 0 1 2-2z"/></svg>555-219-8063</span>
      <span>http://www.brightwirenet.example</span>
    </div>
  </div>

  <div class="divider"></div>

  <div class="back-brand">
    <div class="brand__row"><span class="brand__dot"></span><span class="brand__name">Kornwell, Inc.</span></div>
    <div class="brand__url">www.kornwell.example</div>
    <div class="brand__tag">Internet Services</div>
    <div class="brand__phone">(555) 304-7712</div>
  </div>

  <div class="stamp"></div>
  <div class="address-line" style="top:210px"></div>
  <div class="address-line" style="top:236px"></div>
  <div class="address-line" style="top:262px"></div>
</section>

</body>
</html>
```